New Company Business Card Design

I have a new company logo and I want a new business card design. I dont know if the logo file i attached is in the correct format or quality. We are a New York City Specialty construction Firm specializing in high risk out of the box projects. I want a simple and classy business card that people will his card is as crisp as the work his company does.

Target Market(s)

Clients in the heavy construction industry in New York City

Industry/Entity Type

Construction Company

Contact Information for Business Card

Simple Classy - DIFFERENT

Font styles to use
Other font styles liked:
• Mach the logo font in some way

Colors

Designer to choose colors to be used in the design.

Requirements
Must have
• Uniqueness
Nice to have
• Nothing particular - Just different and classy - Timeless
Should not have
• Goofy Shit or Gimmicky shit

```html
<!DOCTYPE html>
<html lang="en">
<head>
<meta charset="utf-8">
<title>Halvorsen Works – Business Card</title>
<link href="https://fonts.googleapis.com/css2?family=Montserrat:wght@500;700;800&family=Questrial&display=swap" rel="stylesheet">
<style>
  :root {
    --bg: #e9eaec;
    --paper: #fbfbfb;
    --brand-blue: #1c64c4;
    --edge-blue: #1b5fb8;
    --ink: #111418;
    --muted: #2a2e33;
  }
  * { margin: 0; padding: 0; box-sizing: border-box; }
  html, body {
    width: 1200px; height: 1021px; overflow: hidden;
    background: var(--bg);
  }
  .sheet {
    width: 1200px; height: 1021px;
    display: flex; align-items: center; justify-content: center; gap: 32px;
  }
  .card {
    position: relative;
    width: 560px; height: 320px;
    background: var(--paper);
    border-bottom: 5px solid var(--edge-blue);
    box-shadow: 0 14px 30px rgba(0,0,0,0.16), 0 2px 6px rgba(0,0,0,0.08);
  }
  .wordmark {
    display: flex; align-items: center; gap: 10px;
    font-family: 'Montserrat', sans-serif;
    font-weight: 800;
    color: var(--brand-blue);
    line-height: 1;
    letter-spacing: 0.02em;
  }
  .wordmark-square {
    width: 14px; height: 14px; background: var(--brand-blue); flex: none;
  }
  /* front */
  .card-front {
    display: flex; flex-direction: column; align-items: center; justify-content: center;
  }
  .card-front .wordmark { font-size: 34px; }
  .card-front .site {
    margin-top: 26px;
    font-family: 'Questrial', sans-serif;
    font-size: 15px; letter-spacing: 0.16em;
    color: var(--brand-blue);
  }
  /* back */
  .card-back .wordmark {
    position: absolute; top: 42px; right: 38px;
    font-size: 22px;
  }
  .card-back .wordmark-square { width: 10px; height: 10px; }
  .person {
    position: absolute; left: 40px; top: 120px;
  }
  .person-name {
    font-family: 'Montserrat', sans-serif; font-weight: 700;
    font-size: 24px; letter-spacing: -0.01em; color: var(--ink);
  }
  .person-title {
    margin-top: 4px;
    font-family: 'Questrial', sans-serif; font-size: 16px;
    color: var(--brand-blue);
  }
  .contacts {
    position: absolute; left: 40px; bottom: 34px;
    list-style: none;
    font-family: 'Questrial', sans-serif; font-size: 15px; color: var(--muted);
  }
  .contacts li { display: flex; align-items: center; gap: 10px; height: 24px; }
  .contacts svg { width: 14px; height: 14px; flex: none; }
</style>
</head>
<body>
<main class="sheet">
  <section class="card card-front" aria-label="Card front">
    <div class="wordmark"><span class="wordmark-square"></span>HALVORSEN WORKS, INC.</div>
    <p class="site">www.yourwebsite.com</p>
  </section>

  <section class="card card-back" aria-label="Card back">
    <div class="wordmark"><span class="wordmark-square"></span>HALVORSEN WORKS, INC.</div>
    <div class="person">
      <p class="person-name">YOUR NAME</p>
      <p class="person-title">Job Title</p>
    </div>
    <ul class="contacts">
      <li>
        <svg viewBox="0 0 14 14" aria-hidden="true"><rect x="3.5" y="0.8" width="7" height="12.4" rx="1.3" fill="none" stroke="var(--brand-blue)" stroke-width="1.3"/><circle cx="7" cy="11" r="0.8" fill="var(--brand-blue)"/></svg>
        000 000 0000
      </li>
      <li>
        <svg viewBox="0 0 14 14" aria-hidden="true"><rect x="0.8" y="2.8" width="12.4" height="8.4" fill="var(--brand-blue)"/><path d="M1 3.2 L7 8 L13 3.2" fill="none" stroke="#fff" stroke-width="1.1"/></svg>
        youremail@xyz.com
      </li>
      <li>
        <svg viewBox="0 0 14 14" aria-hidden="true" fill="none" stroke="var(--brand-blue)" stroke-width="1.1"><circle cx="7" cy="7" r="6"/><ellipse cx="7" cy="7" rx="2.6" ry="6"/><path d="M1 7h12M2 4h10M2 10h10"/></svg>
        www.yourwebsite.com
      </li>
    </ul>
  </section>
</main>
</body>
</html>
```